Retirement Plan Advisor Bio

See the attached document and photo for content. I would like someone to design this one page flyer using my logo. This logo was designed by a designer with sketch hive. I am looking for a professional looking document. I want to he color scheme to be primarily white and gold.

Target Market(s)

Employers who offer a retirement plan

Requirements
Should not have
• The designs that I have received look more like resumes. I am interested in advertising my Retirement plan services. If anyone can change their submissions and change it to an ad for retirement plan services instead of a Bio or resume, I would prefer that.

```html
<!DOCTYPE html>
<html lang="en">
<head>
<meta charset="utf-8">
<title>Helen R Marsh – Retirement Plan Advisor</title>
<link href="https://fonts.googleapis.com/css2?family=Arimo:wght@400;700&family=Lato:wght@300;400;700;900&display=swap" rel="stylesheet">
<style>
  :root {
    --gold: #b4965c;
    --gold-panel: #c9b27c;
    --gold-line: #c2a66e;
    --ink: #2a2a2a;
    --body: #3a3a3a;
    --muted: #8a8a8a;
    --side: #f2f2f2;
    --dark: #25292a;
    --white: #ffffff;
  }
  * { margin: 0; padding: 0; box-sizing: border-box; }
  html, body { width: 840px; height: 1200px; overflow: hidden; background: var(--white); }
  .flyer { position: relative; width: 840px; height: 1200px; background: var(--white); font-family: "Arimo", Arial, sans-serif; color: var(--body); }
  .side-column { position: absolute; left: 561px; top: 0; width: 279px; height: 1180px; background: var(--side); }
  .brand-block { position: absolute; left: 0; top: 40px; width: 33px; height: 114px; background: var(--gold); }
  .brand-name { position: absolute; left: 56px; top: 92px; display: flex; align-items: center; gap: 10px; font-family: "Lato", sans-serif; font-weight: 400; font-size: 24px; color: var(--gold); letter-spacing: 0.5px; }
  .brand-name .mark { width: 16px; height: 16px; background: var(--gold); }
  .header-rule { position: absolute; left: 33px; top: 154px; width: 807px; height: 2px; background: var(--gold-line); }
  .accent-bar { position: absolute; left: 34px; top: 181px; width: 8px; height: 677px; background: var(--gold); }
  .accent-bar-dark { position: absolute; left: 34px; top: 858px; width: 8px; height: 176px; background: var(--dark); }
  .section-title { position: absolute; font-family: "Lato", sans-serif; font-weight: 400; font-size: 17px; letter-spacing: 5px; color: var(--gold); }
  .section-rule { position: absolute; height: 1px; background: var(--gold-line); }
  .copy { position: absolute; font-size: 15px; line-height: 26px; color: var(--body); }
  .list { position: absolute; list-style: none; font-size: 15px; color: var(--body); }
  .list li { padding-left: 12px; text-indent: -12px; line-height: 26px; }
  .list li::before { content: "» "; font-size: 11px; }
  .list.spaced li { line-height: 30px; }
  .degree { position: absolute; left: 70px; top: 869px; font-size: 15px; font-weight: 700; color: var(--ink); }
  .disclosure { position: absolute; left: 70px; top: 897px; font-size: 15px; line-height: 30px; color: var(--body); }
  .site-footer { position: absolute; right: 307px; top: 1080px; font-size: 17px; font-weight: 700; letter-spacing: 1.5px; color: var(--ink); }
  .portrait { position: absolute; left: 565px; top: 333px; width: 275px; height: 393px; background: linear-gradient(180deg, #6f7d9c 0%, #5d6c8e 45%, #2f3236 75%, #1f2122 100%); }
  .name-panel { position: absolute; left: 565px; top: 726px; width: 275px; height: 115px; background: var(--gold-panel); padding: 30px 0 0 11px; }
  .name-panel .name { font-family: "Lato", sans-serif; font-weight: 300; font-size: 22px; color: #4d4638; }
  .name-panel .name sup { font-size: 11px; }
  .name-panel .role { font-family: "Lato", sans-serif; font-weight: 300; font-size: 16px; color: #f5efe2; margin-top: 6px; }
  .contact-list { position: absolute; left: 596px; top: 868px; list-style: none; font-family: "Lato", sans-serif; font-weight: 400; font-size: 15px; color: var(--muted); }
  .contact-list li { display: flex; align-items: flex-start; gap: 20px; margin-bottom: 12px; line-height: 19px; }
  .contact-list svg { width: 24px; height: 20px; flex: none; }
  .contact-rule { position: absolute; left: 594px; top: 1033px; width: 184px; height: 4px; background: var(--dark); }
  .base-band { position: absolute; left: 0; top: 1180px; width: 840px; height: 20px; background: var(--dark); }
</style>
</head>
<body>
<main class="flyer">
  <div class="side-column"></div>
  <div class="brand-block"></div>
  <div class="brand-name"><span class="mark"></span>Crestline Financial, LLC</div>
  <div class="header-rule"></div>
  <div class="accent-bar"></div>
  <div class="accent-bar-dark"></div>

  <h2 class="section-title" style="left:74px;top:186px;">ABOUT ME</h2>
  <div class="section-rule" style="left:74px;top:216px;width:379px;"></div>
  <p class="copy" style="left:78px;top:227px;width:420px;">I strive to improve retirement outcomes for my plan sponsor clients and their employees through careful retirement plan design assistance, strategic and targeted communication and education , as well as continual monitoring of results.</p>

  <h2 class="section-title" style="left:74px;top:383px;">PROFESSIONAL SPECIALTIES</h2>
  <div class="section-rule" style="left:74px;top:412px;width:379px;"></div>
  <ul class="list" style="left:78px;top:430px;width:460px;">
    <li>Over 18 years of experience in the retirement plan industry</li>
    <li>Focused on helping plan sponsors reduce administrative burdens and fiduciary risk</li>
    <li>Dedicated to helping employees work toward a positive retirement outcome through careful analysis of their savings rate , investment strategy and overall financial wellness</li>
  </ul>

  <h2 class="section-title" style="left:65px;top:611px;">QUALIFICATIONS</h2>
  <div class="section-rule" style="left:65px;top:640px;width:379px;"></div>
  <ul class="list spaced" style="left:78px;top:644px;width:470px;">
    <li>Certified Retirement Planner</li>
    <li>Accredited Plan Fiduciary</li>
    <li>Investment Advisor Representative</li>
    <li>Series 7, 63, and 65 Securities licenses with Harbor Securities</li>
    <li>Holds Life and Health Insurance licenses from Illinois</li>
  </ul>

  <h2 class="section-title" style="left:65px;top:827px;">EDUCATION</h2>
  <div class="section-rule" style="left:65px;top:856px;width:379px;"></div>
  <p class="degree">BS Whitmore University, 1987</p>
  <p class="disclosure">*Securities and Investment Advisory Services offered<br>&nbsp;through Harbor Securities Holdings, Inc, a Registered<br>&nbsp;Broker/Dealer and Investment Advisor,<br>&nbsp;member NFSA/ICPS</p>

  <p class="site-footer">www.helenmarsh.com</p>

  <div class="portrait" role="img" aria-label="Portrait photograph of the advisor in a dark blazer against a blue studio backdrop"></div>
  <div class="name-panel">
    <p class="name">Helen R Marsh CRP<sup>®</sup> APF<sup>®</sup></p>
    <p class="role">Harbor Securities Advisor</p>
  </div>

  <ul class="contact-list">
    <li><svg viewBox="0 0 24 20" fill="none" stroke="#8a8a8a" stroke-width="1.4"><rect x="2" y="4" width="20" height="13" rx="1"/><path d="M2 5l10 7 10-7"/></svg>helen.marsh@harborsec.com</li>
    <li><svg viewBox="0 0 24 20" fill="none" stroke="#8a8a8a" stroke-width="1.4"><path d="M5 2l4 4-2 3c1.5 3 3.5 5 6 6l3-2 4 4-2 2C11 19 4 12 3 4z"/></svg>(555)210.4820</li>
    <li><svg viewBox="0 0 24 20" fill="none" stroke="#8a8a8a" stroke-width="1.4"><path d="M12 19s-6-6.5-6-11a6 6 0 0112 0c0 4.5-6 11-6 11z"/><circle cx="12" cy="8" r="2.2"/></svg>250 Meadow Ln.<br>Fairview, IL 60400</li>
    <li><svg viewBox="0 0 24 20" fill="none" stroke="#8a8a8a" stroke-width="1.4"><circle cx="12" cy="10" r="8.5"/><ellipse cx="12" cy="10" rx="3.8" ry="8.5"/><path d="M3.5 10h17M5 5.5h14M5 14.5h14"/></svg>www.helenmarsh.com</li>
  </ul>
  <div class="contact-rule"></div>

  <div class="base-band"></div>
</main>
</body>
</html>
```